Women's Health Company needs business card

We need a business card for a USA based women's health care company. We use digital technology to enhance therapy prescribed by clinicians for their patients

```html
<!DOCTYPE html>
<html lang="en">
<head>
<meta charset="utf-8">
<title>Velora Health — Business Card</title>
<link href="https://fonts.googleapis.com/css2?family=Source+Sans+3:wght@400;600&display=swap" rel="stylesheet">
<style>
  :root {
    --backdrop: #e4e4e4;
    --purple: #8b5299;
    --teal: #6fb8b5;
    --card-white: #f4f4f4;
    --ink: #2a2a2a;
    --font: "Source Sans 3", sans-serif;
  }
  * { box-sizing: border-box; margin: 0; padding: 0; }
  html, body {
    width: 1200px;
    height: 960px;
    overflow: hidden;
    background: var(--backdrop);
    font-family: var(--font);
  }
  .canvas { position: relative; width: 1200px; height: 960px; }
  .card {
    position: absolute;
    left: 296px;
    width: 608px;
    height: 348px;
    overflow: hidden;
  }
  .card--front { top: 112px; background: var(--purple); }
  .card--back { top: 513px; background: var(--card-white); }

  .wordmark {
    position: absolute;
    display: flex;
    align-items: center;
    gap: 10px;
    color: var(--teal);
    font-weight: 400;
    white-space: nowrap;
    line-height: 1;
  }
  .wordmark__dot {
    border-radius: 50%;
    background: var(--teal);
    flex: none;
  }
  .card--front .wordmark {
    left: 0; right: 0; top: 144px;
    justify-content: center;
    font-size: 62px;
    letter-spacing: 1px;
  }
  .card--front .wordmark__dot { width: 14px; height: 14px; }
  .card--back .wordmark {
    left: 44px; top: 158px;
    font-size: 38px;
  }
  .card--back .wordmark__dot { width: 10px; height: 10px; }

  .divider {
    position: absolute;
    left: 302px; top: 85px;
    width: 2px; height: 178px;
    background: var(--purple);
  }
  .contact {
    position: absolute;
    left: 340px; top: 86px;
    color: var(--ink);
    font-size: 15.5px;
    line-height: 20.5px;
  }
  .contact__name {
    color: var(--teal);
    font-weight: 600;
    font-size: 20px;
    line-height: 24px;
  }
  .contact__role { font-size: 16px; line-height: 20px; margin-bottom: 26px; }
  .contact__address-end { margin-bottom: 5px; }
  .contact__line { display: flex; align-items: center; gap: 5px; }
  .contact__icon { width: 14px; height: 14px; flex: none; }

  .footer-band {
    position: absolute;
    left: 0; right: 0; bottom: 0;
    height: 66px;
    background: linear-gradient(180deg, var(--teal) 0%, var(--purple) 100%);
  }
</style>
</head>
<body>
<main class="canvas">
  <section class="card card--front" aria-label="Card front">
    <div class="wordmark"><span class="wordmark__dot"></span>Velora Health</div>
  </section>

  <section class="card card--back" aria-label="Card back">
    <div class="footer-band" role="img" aria-label="Decorative teal and purple wave band along the bottom edge"></div>

    <div class="wordmark"><span class="wordmark__dot"></span>Velora Health</div>

    <div class="divider"></div>

    <div class="contact">
      <p class="contact__name">Daniel Reyes</p>
      <p class="contact__role">Founder</p>
      <p>418 Harbor Lane, Suite 120</p>
      <p class="contact__address-end">Tampa, Florida, 33602</p>
      <p class="contact__line">
        <svg class="contact__icon" viewBox="0 0 14 14" aria-hidden="true"><path fill="none" stroke="var(--purple)" stroke-width="1.4" d="M3 1.5 L5 4.5 L3.8 5.8 C4.6 7.6 6.4 9.4 8.2 10.2 L9.5 9 L12.5 11 L11 12.6 C6.5 12.5 1.5 7.5 1.4 3 Z"/></svg>
        (555) 014-2276
      </p>
      <p class="contact__line">
        <svg class="contact__icon" viewBox="0 0 14 14" aria-hidden="true"><rect x="1.5" y="3" width="11" height="8" fill="none" stroke="var(--purple)" stroke-width="1.3"/><path d="M1.5 3 L7 7.5 L12.5 3" fill="none" stroke="var(--purple)" stroke-width="1.3"/></svg>
        daniel@velorahealth.com
      </p>
      <p class="contact__line">
        <svg class="contact__icon" viewBox="0 0 14 14" aria-hidden="true"><g fill="none" stroke="var(--purple)" stroke-width="1.1"><circle cx="7" cy="7" r="5.5"/><ellipse cx="7" cy="7" rx="2.4" ry="5.5"/><path d="M1.5 7 H12.5 M2.5 4.3 H11.5 M2.5 9.7 H11.5"/></g></svg>
        www.velorahealth.com
      </p>
    </div>
  </section>
</main>
</body>
</html>
```